Honey Jar Label

I am looking for a logo for a 6oz. glass honey jar with a black lid that will contain honey from our bee boxes.
+ our product name is:  Clover Meadow Honey
+ the label must include a Nutrition Facts label (google 'honey nutrition facts label' images for what to use).
+ dimensions:	 8 x 2.1875 inches (w x h)
+ color:	We can do one, two or three color prints. Use the PANTONE MATCHING SYSTEM (PMS)
+ file types:  must be Adobe file (AI, PDF, PSD) or EPS files. We cannot accept other file types.
+ notes:	Gradients and halftones are strongly discouraged
+ provide all fonts with file or convert to outlines
+ design files must be CMYK, 300 dpi at 100%.

```html
<!DOCTYPE html>
<html lang="en">
<head>
<meta charset="utf-8">
<title>Clover Meadow Honey — Jar Label</title>
<link href="https://fonts.googleapis.com/css2?family=Quicksand:wght@300&family=PT+Sans:wght@400;700&display=swap" rel="stylesheet">
<style>
  :root {
    --paper: #ffffff;
    --ink: #111111;
    --honey-yellow: #ffe600;
    --pale-yellow: #ffff66;
    --cream: #fffcc0;
    --amber: #ffd600;
    --orange: #ff7f00;
    --label-edge: #9a9a9a;
  }
  * { box-sizing: border-box; margin: 0; padding: 0; }
  html, body {
    width: 1200px; height: 859px; overflow: hidden;
    background: var(--paper);
  }
  .canvas { position: relative; width: 1200px; height: 859px; }

  /* Brand wordmark */
  .wordmark {
    position: absolute;
    font-family: "Quicksand", sans-serif;
    font-weight: 300;
    color: var(--ink);
    letter-spacing: -0.01em;
  }
  .wordmark .line { display: block; white-space: nowrap; }
  .wordmark .dot {
    position: absolute; border-radius: 50%;
    background: var(--honey-yellow);
  }
  .wordmark--primary { left: 478px; top: 146px; font-size: 96px; line-height: 83px; }
  .wordmark--primary .dot { width: 46px; height: 46px; left: -56px; top: 18px; }
  .wordmark--label { left: 500px; top: 546px; font-size: 37px; line-height: 37px; }
  .wordmark--label .dot { width: 18px; height: 18px; left: -22px; top: 6px; }

  /* Jar label strip */
  .jar-label {
    position: absolute; left: 276px; top: 522px;
    width: 629px; height: 173px;
    border: 1px solid var(--label-edge);
    background: var(--paper);
    overflow: hidden;
  }
  .comb-field { position: absolute; }
  .comb-field--right {
    right: 0; top: 0; width: 310px; height: 100%;
    background: linear-gradient(135deg, var(--cream) 0%, var(--pale-yellow) 30%, var(--amber) 55%, var(--orange) 80%, var(--honey-yellow) 100%);
    clip-path: polygon(14% 0, 100% 0, 100% 100%, 0 100%, 0 55%);
  }
  .comb-field--left {
    left: 0; top: 55px; width: 180px; height: 118px;
    background: linear-gradient(90deg, var(--orange) 0%, var(--pale-yellow) 35%, var(--amber) 70%, var(--cream) 100%);
  }
  .comb-field--base {
    left: 180px; bottom: 0; width: 150px; height: 14px;
    background: linear-gradient(90deg, var(--amber), var(--cream), var(--orange));
  }

  /* Nutrition facts panel */
  .nutrition {
    position: absolute; left: 47px; top: 9px;
    width: 105px; height: 156px;
    background: var(--pale-yellow);
    padding: 3px 6px 0 6px;
    font-family: "PT Sans", sans-serif;
    color: var(--ink);
    font-size: 7px; line-height: 1.2;
  }
  .nutrition__title { font-weight: 700; font-size: 12px; line-height: 12px; text-align: center; }
  .nutrition__serving { text-align: center; font-size: 7px; }
  .nutrition__rule { background: var(--ink); margin: 1px 0; }
  .nutrition__rule--thick { height: 5px; }
  .nutrition__rule--mid { height: 3px; }
  .nutrition__rule--thin { height: 1px; }
  .nutrition__small { font-size: 5px; }
  .nutrition__row { display: flex; justify-content: space-between; }
  .nutrition__row--right { justify-content: flex-end; font-size: 5px; }
  .nutrition__row--indent { padding-left: 5px; }
  .nutrition b { font-weight: 700; }
  .nutrition__footnote { font-size: 5px; line-height: 1.3; margin-top: 4px; }
</style>
</head>
<body>
<main class="canvas">

  <h1 class="wordmark wordmark--primary">
    <span class="dot"></span>
    <span class="line">Clover</span>
    <span class="line">Meadow</span>
    <span class="line">Honey</span>
  </h1>

  <section class="jar-label" aria-label="Honey jar wrap label">
    <div class="comb-field comb-field--left" role="img" aria-label="Honeycomb pattern in yellow and orange"></div>
    <div class="comb-field comb-field--base" role="img" aria-label="Honeycomb pattern in yellow and orange"></div>
    <div class="comb-field comb-field--right" role="img" aria-label="Honeycomb pattern in yellow, cream and orange"></div>

    <div class="nutrition">
      <div class="nutrition__title">Nutrition Facts</div>
      <div class="nutrition__serving">Serving Size 1 Tbsp (21g)</div>
      <div class="nutrition__serving">Servings Per Container 00</div>
      <div class="nutrition__rule nutrition__rule--thick"></div>
      <div class="nutrition__small">Amount Per Serving</div>
      <div class="nutrition__rule nutrition__rule--thin"></div>
      <div>Calories 60</div>
      <div class="nutrition__rule nutrition__rule--mid"></div>
      <div class="nutrition__row nutrition__row--right">%Daily Value*</div>
      <div class="nutrition__rule nutrition__rule--thin"></div>
      <div class="nutrition__row"><span><b>Total Fat</b> 0g</span><span>0%</span></div>
      <div class="nutrition__row"><span><b>Sodium</b> 0mg</span><span>0%</span></div>
      <div class="nutrition__row"><span><b>Total Carb.</b> 17g</span><span>6%</span></div>
      <div class="nutrition__row nutrition__row--indent"><span>Sugars 16g</span></div>
      <div class="nutrition__row"><span><b>Protein</b> 0g</span><span>0%</span></div>
      <div class="nutrition__rule nutrition__rule--thick"></div>
      <div class="nutrition__footnote">*Percent Daily Values (DV) are based on 2,000 calorie diet.</div>
    </div>
  </section>

  <p class="wordmark wordmark--label">
    <span class="dot"></span>
    <span class="line">Clover</span>
    <span class="line">Meadow</span>
    <span class="line">Honey</span>
  </p>

</main>
</body>
</html>
```